VFX Company Business Card Design Project

The Ember Vale is a decentralized Visual Effects Studio servicing the television and feature film industries.
Project Brief:
Take our logo that was previously designed on Pixel Harbor and make a double sided business card.
Requirements:
- Card MUST be double sided.
- Front of card MUST have the yellow part of our logo against the dark grey background.
- Back of card is completely up to the designer.
- Back of card must include the complete company logo.
Please follow these File Preparation guidelines:
http://printmoor.example/infopage?file=filetype_en&s=PrintMoor_new&lang=en
Industry/Entity Type
Business
Look and feel
Each slider illustrates characteristics of the customer's brand and the style your logo design should communicate.

```html
<!DOCTYPE html>
<html lang="en">
<head>
<meta charset="utf-8">
<title>The Ember Vale – Business Card</title>
<link rel="stylesheet" href="https://fonts.googleapis.com/css2?family=Quicksand:wght@400;500;600&display=swap">
<style>
  :root {
    --backdrop: #3a3d3c;
    --card-dark: #2f2f30;
    --card-light: #f4f4f3;
    --gold: #e9bb2a;
    --logo-grey: #8c979b;
    --ink: #2b2b2b;
    --ink-soft: #6d6d6d;
    --icon-dark: #2a2a2a;
  }
  html, body {
    margin: 0;
    width: 1200px;
    height: 900px;
    overflow: hidden;
    background: var(--backdrop);
    font-family: "Quicksand", sans-serif;
  }
  .canvas {
    width: 1200px;
    height: 900px;
    display: flex;
    flex-direction: column;
    align-items: center;
    justify-content: center;
    gap: 44px;
  }
  .card {
    width: 630px;
    height: 360px;
    position: relative;
    box-sizing: border-box;
    box-shadow: 0 10px 24px rgba(0,0,0,0.35);
  }
  .card--front {
    background: var(--card-dark);
    display: flex;
    align-items: center;
    justify-content: center;
  }
  .brand {
    display: flex;
    align-items: center;
    gap: 18px;
  }
  .brand__dot {
    width: 46px;
    height: 46px;
    border-radius: 50%;
    background: var(--gold);
  }
  .brand__name {
    font-weight: 600;
    color: var(--logo-grey);
    font-size: 44px;
    letter-spacing: 1px;
  }
  .card--back {
    background: var(--card-light);
    padding: 34px 36px;
    color: var(--ink);
  }
  .card--back .brand { gap: 12px; }
  .card--back .brand__dot { width: 28px; height: 28px; }
  .card--back .brand__name { font-size: 26px; }
  .identity {
    margin-top: 30px;
    width: 290px;
    border-top: 1.5px solid var(--gold);
    border-bottom: 1.5px solid var(--gold);
    padding: 10px 0 8px;
  }
  .identity__name {
    font-size: 25px;
    font-weight: 500;
    letter-spacing: 1.5px;
    text-transform: uppercase;
    margin: 0;
  }
  .identity__role {
    font-size: 14px;
    color: var(--ink-soft);
    margin: 2px 0 0;
  }
  .contacts {
    position: absolute;
    left: 36px;
    bottom: 30px;
    list-style: none;
    margin: 0;
    padding: 0;
    font-size: 14px;
  }
  .contacts li {
    display: flex;
    align-items: center;
    gap: 14px;
    height: 20px;
  }
  .contacts svg { width: 13px; height: 13px; flex: none; }
  .highlight { color: var(--gold); }
  .address {
    position: absolute;
    right: 40px;
    bottom: 52px;
    font-size: 14px;
    line-height: 20px;
    text-align: left;
    margin: 0;
    font-style: normal;
  }
</style>
</head>
<body>
<main class="canvas">
  <section class="card card--front" aria-label="Card front">
    <div class="brand">
      <span class="brand__dot"></span>
      <span class="brand__name">The Ember Vale</span>
    </div>
  </section>

  <section class="card card--back" aria-label="Card back">
    <div class="brand">
      <span class="brand__dot"></span>
      <span class="brand__name">The Ember Vale</span>
    </div>
    <div class="identity">
      <h1 class="identity__name">Daniel Harlow</h1>
      <p class="identity__role">Director</p>
    </div>
    <ul class="contacts">
      <li>
        <svg viewBox="0 0 14 14" aria-hidden="true"><circle cx="7" cy="7" r="7" fill="var(--icon-dark)"/><path d="M4.5 3.5l1.5 0 .6 2-1 .8a5 5 0 0 0 2.1 2.1l.8-1 2 .6v1.5c0 .6-.5 1-1 1A6 6 0 0 1 3.5 4.5c0-.5.4-1 1-1z" fill="var(--gold)"/></svg>
        +1 555 014 2786
      </li>
      <li>
        <svg viewBox="0 0 14 14" aria-hidden="true"><circle cx="7" cy="7" r="7" fill="var(--icon-dark)"/><rect x="3.5" y="4.5" width="7" height="5" fill="none" stroke="var(--gold)" stroke-width="1"/><path d="M3.5 4.5L7 7.3l3.5-2.8" fill="none" stroke="var(--gold)" stroke-width="1"/></svg>
        hello@embervale.example
      </li>
      <li>
        <svg viewBox="0 0 14 14" aria-hidden="true"><circle cx="7" cy="7" r="7" fill="var(--icon-dark)"/><circle cx="7" cy="7" r="2.4" fill="var(--gold)"/></svg>
        social.example/@EmberVale
      </li>
      <li>
        <svg viewBox="0 0 14 14" aria-hidden="true"><circle cx="7" cy="7" r="7" fill="var(--icon-dark)"/><circle cx="7" cy="7" r="3.5" fill="none" stroke="var(--gold)" stroke-width="1"/><path d="M3.5 7h7M7 3.5c-1.6 2-1.6 5 0 7M7 3.5c1.6 2 1.6 5 0 7" fill="none" stroke="var(--gold)" stroke-width="0.8"/></svg>
        <span>www.<span class="highlight">embervale</span>.example</span>
      </li>
    </ul>
    <address class="address">42 Foundry Lane Unit C<br>Lindell Harbor, FL 30100</address>
  </section>
</main>
</body>
</html>
```